Call for Garage Door Service Label

Design a label to attached to garage doors that has our information for customer to contact us for service. there should be two designs. one that is focused on residential clients, the other is focused on commercial clients. the sticker size should be 5" wide by 4" high. Note for the designer not the label - for more info please visit our website kelz.ca or ask me

Target Market(s)

One for Residential and One for commercial

Industry/Entity Type

Overhead Garage doors

Colors

Designer to choose colors to be used in the design.

Requirements
Must have
• My Logo, My Phone Number (should be large and easy to see), My email sales@kelz.ca, My website www.kelz.ca

```html
<!DOCTYPE html>
<html lang="en">
<head>
<meta charset="utf-8">
<title>Kelz Overhead Door – Service Label</title>
<link rel="stylesheet" href="https://fonts.googleapis.com/css2?family=Anton&display=swap">
<style>
  :root {
    --maroon: #4a1018;
    --slate: #37474a;
    --sage: #4a5c4a;
    --paper: #ffffff;
  }
  html, body {
    margin: 0;
    padding: 0;
    overflow: hidden;
    background: var(--paper);
  }
  .label {
    position: relative;
    width: 1200px;
    height: 960px;
    box-sizing: border-box;
    border: 23px solid var(--maroon);
    background: var(--paper);
    font-family: "Anton", "Oswald", sans-serif;
    text-transform: uppercase;
    overflow: hidden;
  }
  .brand {
    position: absolute;
    top: 78px;
    left: 0;
    right: 0;
    display: flex;
    align-items: center;
    justify-content: center;
    gap: 22px;
    color: var(--maroon);
  }
  .brand-mark {
    width: 56px;
    height: 56px;
    background: var(--maroon);
    flex: none;
  }
  .brand-name {
    font-size: 92px;
    line-height: 1;
    letter-spacing: 3px;
    text-align: center;
  }
  .brand-name span { display: block; }
  .tagline {
    position: absolute;
    top: 388px;
    left: 0;
    right: 0;
    margin: 0;
    text-align: center;
    color: var(--sage);
    font-size: 53px;
    line-height: 1.43;
    font-weight: 400;
  }
  .phone {
    position: absolute;
    top: 548px;
    left: 0;
    right: 0;
    text-align: center;
    color: var(--maroon);
    font-size: 146px;
    line-height: 1.1;
    letter-spacing: 1px;
  }
  .contact {
    position: absolute;
    left: 0;
    right: 0;
    text-align: center;
    font-size: 50px;
    line-height: 1;
    margin: 0;
  }
  .contact .key { color: var(--slate); }
  .contact .value { color: var(--maroon); }
  .contact-web { top: 752px; }
  .contact-email { top: 828px; }
</style>
</head>
<body>
  <main class="label">
    <header class="brand">
      <div class="brand-mark" aria-hidden="true"></div>
      <div class="brand-name"><span>Kelz Overhead</span><span>Door</span></div>
    </header>

    <p class="tagline">The best garage door solutions for your<br>home and business needs.</p>

    <div class="phone">(519) 555-0147</div>

    <p class="contact contact-web"><span class="key">Website: </span><span class="value">www.kelz.ca</span></p>
    <p class="contact contact-email"><span class="key">Email: </span><span class="value">sales@kelz.ca</span></p>
  </main>
</body>
</html>
```